Radiology Department needs a series of 3 facebook posts - similar design

We need a series of 3 posts for our facebook page, each one presenting the activity of one of 3 physicians.
The main design elements can be the same, the only thing that will change between posts will be the field of activity and name of the physician and the representative image of its activity.
If needed the design elements can be slightly different between posts for better adjustment to the representative images.
You can find as an attachment:
- Manual of institutional identity of the Hospital (Velmor Clinica)
- Our facebook cover page
- Our department video
- The representative images for each post, identified with the name of each physician
- The Institutional identity manual with the logo of "Brisa Medical School" - just for Dr Tomas Brandilo post.
So, each one of the three posts should state the name and field of activity of each physician, including somehow the corresponding representative image, and should have background innovative design elements.
Post 1:
Name of the physician: Prof. Doutor Rui Castelvo
Field of activity: Imagiologia Reumatológica e do Sistema Músculo-Esquelético
Image as an attachment
Post 2:
Name of the physician: Prof.ª Doutora Inês Barroca
Field of activity: Imagiologia Cardíaca
Image as an attachment
Post 3:
Name of the physician: Dr. Tomas Lupo
Field of activity: Tese de Doutoramento em Curso - Identificação da Lesão Cartilagínea Precoce. Com orientação do Prof. Doutor Rui Castelvo e Prof.ª Doutora Inês Sofia Carvalhal.
Image as an attachment
Just for Dr Tomas Lupo, the logo of Brisa Medical School should also be included (please check the corresponding institutional identity manual that was just added in documents).
Updates

Just for Dr Tomas Brandilo, the logo of Brisa Medical School should also be included (please check the corresponding institutional identity manual that was just added in documents).

Please note that we are just looking for 3 facebook POSTS, not facebook cover page, thanks.

Please kindly note that we are looking for facebook POST and NOT facebook cover page.

Target Market(s)

General Population

Industry/Entity Type

Health

Font styles to use
Other font styles liked:
• Check manual of institutional identity and try to approach if appropriate

Requirements
Must have
• Check project description.
Nice to have
• If the designer finds appropriate, the logo of the Hospital would be nice in all the three posts, the most simple one just stating "VelmorClinica" - please check the attached manual of institutional identity

```html
<!DOCTYPE html>
<html lang="pt">
<head>
<meta charset="utf-8">
<title>Prof. Doutor Rui Castelvo — Imagiologia Reumatológica</title>
<link rel="stylesheet" href="https://fonts.googleapis.com/css2?family=Montserrat:wght@400;500;600;700&family=Open+Sans:wght@400&family=Roboto+Condensed:wght@700&display=swap">
<style>
  :root {
    --navy: #1b3566;
    --black: #000000;
    --light: #e4e6e3;
    --gold: #f0b323;
    --white: #ffffff;
    --placeholder: #e6e6e6;
    --placeholder-text: #a9a9a9;
    --ink: #1a1a1a;
  }
  html, body { margin: 0; padding: 0; overflow: hidden; }
  body { width: 1200px; height: 627px; background: var(--white); }
  .post {
    position: relative;
    width: 1200px;
    height: 627px;
    overflow: hidden;
    background: var(--navy);
    font-family: "Montserrat", sans-serif;
  }
  .post__shapes { position: absolute; inset: 0; }
  .activity-image {
    position: absolute;
    left: 690px; top: 55px;
    width: 320px; height: 345px;
    background: radial-gradient(ellipse 50% 50% at 50% 45%, rgba(150,150,150,0.9) 0%, rgba(70,70,70,0.6) 45%, rgba(0,0,0,0) 100%);
  }
  .doctor-photo {
    position: absolute;
    left: 77px; top: 36px;
    width: 236px; height: 219px;
    background: var(--placeholder);
    border: 3px solid var(--gold);
    display: flex; align-items: center; justify-content: center;
    font-family: "Roboto Condensed", sans-serif;
    font-weight: 700;
    font-size: 25px;
    color: var(--placeholder-text);
  }
  .school-name {
    position: absolute;
    right: 20px; top: 28px;
    color: var(--white);
    font-weight: 600;
    font-size: 27px;
    letter-spacing: 1px;
  }
  .physician {
    position: absolute;
    left: 80px; top: 284px;
    color: var(--white);
  }
  .physician__title {
    font-weight: 400; font-size: 21px; letter-spacing: 0.5px;
    margin: 0 0 2px;
  }
  .physician__name {
    margin: 0;
    font-weight: 500;
    font-size: 46px;
    line-height: 1.05;
    letter-spacing: 2px;
  }
  .field {
    position: absolute;
    left: 80px; top: 505px;
    margin: 0;
    font-family: "Open Sans", sans-serif;
    font-size: 26px;
    line-height: 36px;
    letter-spacing: 1.6px;
    color: var(--ink);
  }
  .clinic {
    position: absolute;
    right: 32px; top: 436px;
    text-align: right;
    color: var(--navy);
  }
  .clinic__name {
    margin: 0;
    font-weight: 700; font-size: 42px; line-height: 1.1;
  }
  .clinic__tagline {
    margin: 8px 0 0;
    font-weight: 700;
    font-size: 15px;
  }
  .web {
    position: absolute;
    right: 70px; top: 582px;
    color: var(--white);
    font-weight: 600; font-size: 21px; letter-spacing: 2.5px;
  }
</style>
</head>
<body>
<main class="post">
  <svg class="post__shapes" width="1200" height="627" viewBox="0 0 1200 627" aria-hidden="true">
    <polygon points="130,0 1200,105 1200,478 0,168 0,0" fill="var(--black)"/>
    <polygon points="0,492 1200,374 1200,627 0,627" fill="var(--light)"/>
  </svg>

  <div class="activity-image" role="img" aria-label="Angiografia por ressonância magnética das duas mãos"></div>

  <div class="doctor-photo">DOCTOR IMAGE</div>

  <div class="school-name">BRISA MEDICAL SCHOOL</div>

  <section class="physician">
    <p class="physician__title">PROF.</p>
    <h1 class="physician__name">DOUTOR<br>RUI CASTELVO</h1>
  </section>

  <p class="field">Imagiologia Reumatológica e do Sistema<br>Músculo-Esquelético</p>

  <div class="clinic">
    <p class="clinic__name">VelmorClinica</p>
    <p class="clinic__tagline">Cuidamos de si com rigor</p>
  </div>

  <div class="web">www.velmorclinica.pt</div>
</main>
</body>
</html>
```